Corvale Mechanical - Letterhead

We are a plumbing and hvac company based in Calgary. This letterhead will be on our quotes, invoices, preventative maintenance proposals etc.

```html
<!DOCTYPE html>
<html lang="en">
<head>
<meta charset="utf-8">
<title>Corvale Mechanical – Letterhead</title>
<link href="https://fonts.googleapis.com/css2?family=Source+Sans+3:wght@400;600;700;800&display=swap" rel="stylesheet">
<style>
  :root {
    --orange: #f26236;
    --blue: #3a73b8;
    --ink: #333333;
    --backdrop: #e2e2e2;
    --paper: #ffffff;
  }
  * { margin: 0; padding: 0; box-sizing: border-box; }
  html, body { width: 1056px; height: 1200px; overflow: hidden; background: var(--backdrop); }
  body { font-family: "Source Sans 3", "Helvetica Neue", Arial, sans-serif; color: var(--ink); }

  .letterhead {
    position: absolute; left: 104px; top: 0;
    width: 848px; height: 1200px;
    background: var(--paper);
    overflow: hidden;
  }
  .top-rule { position: absolute; left: 0; top: 0; width: 100%; height: 9px; background: var(--orange); }
  .bottom-rule { position: absolute; left: 0; bottom: 0; width: 100%; height: 9px; background: var(--orange); }
  .contact-panel { position: absolute; left: 0; top: 0; width: 848px; height: 172px; }

  .contact-list {
    position: absolute; left: 540px; top: 36px;
    list-style: none; color: #fff; font-size: 14px; line-height: 23.4px;
  }
  .contact-list li { display: flex; align-items: flex-start; }
  .contact-list .icon { width: 14px; height: 14px; margin: 5px 10px 0 0; flex: none; }
  .contact-list .indent { padding-left: 24px; }

  .brand {
    position: absolute; left: 87px; top: 138px;
    display: flex; align-items: center; gap: 10px;
  }
  .brand-dot { width: 22px; height: 22px; border-radius: 50%; background: var(--orange); }
  .brand-name { font-size: 30px; font-weight: 800; color: var(--blue); letter-spacing: 0.3px; }

  .letter { position: absolute; left: 87px; width: 674px; font-size: 12.6px; }
  .date { top: 296px; }
  .recipient { top: 343px; line-height: 23.5px; }
  .salutation { top: 462px; font-size: 18px; font-weight: 700; }
  .body-copy { top: 516px; }
  .body-copy p { line-height: 23.6px; text-align: justify; margin-bottom: 23px; }
  .closing { top: 937px; }
  .signature {
    position: absolute; left: 87px; top: 1000px;
    width: 106px; height: 40px;
    background: linear-gradient(90deg, rgba(58,115,184,0.18), rgba(58,115,184,0.06));
    border-radius: 4px;
  }
</style>
</head>
<body>
<main class="letterhead">
  <div class="top-rule"></div>

  <svg class="contact-panel" viewBox="0 0 848 172" aria-hidden="true">
    <path d="M462 0 H848 V172 H500 Q482 172 479 156 Z" fill="var(--orange)"/>
  </svg>

  <ul class="contact-list">
    <li>
      <svg class="icon" viewBox="0 0 14 14"><circle cx="7" cy="7" r="7" fill="#fff"/><path d="M7 3a2.4 2.4 0 0 0-2.4 2.4C4.6 7.3 7 10.6 7 10.6s2.4-3.3 2.4-5.2A2.4 2.4 0 0 0 7 3z" fill="var(--orange)"/><circle cx="7" cy="5.4" r="0.9" fill="#fff"/></svg>
      <span>410 Harlow Avenue #200</span>
    </li>
    <li class="indent">Calgary, AB T2P 0K4</li>
    <li>
      <svg class="icon" viewBox="0 0 14 14"><circle cx="7" cy="7" r="7" fill="#fff"/><path d="M4.6 3.6l1.4 0 .6 1.8-.9.7a5 5 0 0 0 2.2 2.2l.7-.9 1.8.6 0 1.4c0 .4-.4.7-.8.7A6 6 0 0 1 3.9 4.4c0-.4.3-.8.7-.8z" fill="var(--orange)"/></svg>
      <span>877-555-0142</span>
    </li>
    <li>
      <svg class="icon" viewBox="0 0 14 14"><circle cx="7" cy="7" r="7" fill="#fff"/><rect x="3.5" y="4.5" width="7" height="5" rx="0.6" fill="none" stroke="var(--orange)" stroke-width="1"/><path d="M3.7 4.8 7 7.4l3.3-2.6" fill="none" stroke="var(--orange)" stroke-width="1"/></svg>
      <span>info@corvalemechanical.com</span>
    </li>
    <li>
      <svg class="icon" viewBox="0 0 14 14"><circle cx="7" cy="7" r="7" fill="#fff"/><circle cx="7" cy="7" r="3.6" fill="none" stroke="var(--orange)" stroke-width="1"/><path d="M3.4 7h7.2M7 3.4c-1.6 2-1.6 5.2 0 7.2M7 3.4c1.6 2 1.6 5.2 0 7.2" fill="none" stroke="var(--orange)" stroke-width="0.9"/></svg>
      <span>www.corvalemechanical.com</span>
    </li>
  </ul>

  <div class="brand">
    <span class="brand-dot"></span>
    <span class="brand-name">Corvale Mechanical</span>
  </div>

  <p class="letter date">September 10th, 2020</p>

  <address class="letter recipient" style="font-style:normal">
    First Last Name<br>
    Street Address<br>
    City, State 00000
  </address>

  <p class="letter salutation">Dear Sir / Mam,</p>

  <div class="letter body-copy">
    <p>Lorem ipsum dolor sit amet, consectetur adipiscing elit. Aenean ut ipsum eget massa hendrerit vestibulum vel in velit. Donec pretium neque velit.</p>
    <p>Aliquam porta lectus nec mauris ornare venenatis. Vivamus non est turpis, et cursus sem. Mauris vehicula erat in diam auctor at bibendum nisl lacinia.</p>
    <p>Morbi imperdiet neque vehicula nunc convallis gravida. Vestibulum iaculis pretium placerat. Integer consequat, est sit amet facilisis eleifend, nibh nibh varius orci, eget dapibus arcu dui non purus. Pellentesque in magna mauris. Duis enim sapien, dictum vitae condimentum a, pulvinar vel lacus. Mauris et molestie nibh. Vestibulum vitae nulla at metus elementum porta sit amet interdum elit. Nulla sollicitudin neque eu nulla volutpat congue.</p>
    <p>Etiam pellentesque, velit id dapibus fermentum, turpis sapien ornare dui, ac tincidunt ligula odio congue purus. Nunc sed ante dui, in porta lectus. Cras nec sem lorem. In hac habitasse platea dictumst. Maecenas id diam quis dui porta tristique. Sed id egestas felis. Donec ullamcorper mattis posuere. Phasellus fermentum eleifend tortor vel dapibus. Vestibulum ante ipsum.</p>
  </div>

  <p class="letter closing">Your Sincerely,</p>

  <div class="signature" role="img" aria-label="Handwritten signature"></div>

  <div class="bottom-rule"></div>
</main>
</body>
</html>
```